Discreet simple classy for adult entertainment

I would like a matte black business card with gold writing for my business. Keeping it simple. Having my following:

Lana frost
Events. Entertainment. Promotions
0491726580

or alternatively could have what i had on my previous card below but i think i prefer the above as again - discretion.

Maybe a nice gold line thru the card or some other very simple design . Or not open to ideas/ can be doublesided if any good ideas with that.

included pics of my old bus card. not sure weather i want a photo on it or not. if i do it wont be the same pic. i kinda wanted a card that was discreet so if it was in someones wallet they wouldn't neccessarily realise it was from a stripper.

Target Market(s)

men

Industry/Entity Type

Business

Contact Information for Business Card

Lana frost
0491726580

Requirements
Nice to have
• i don't know i am really open to anything. im giving my cards to guys so something they can have in their wallet that is discreet preferably.

```html
<!DOCTYPE html>
<html lang="en">
<head>
<meta charset="utf-8">
<title>Lana Frost — Business Card</title>
<link href="https://fonts.googleapis.com/css2?family=Poiret+One&family=Josefin+Sans:wght@300;400&display=swap" rel="stylesheet">
<style>
  :root {
    --backdrop: #1b1b1b;
    --card-black: #050505;
    --gold-light: #f3e08a;
    --gold-mid: #d9b43a;
    --gold-deep: #a7801c;
  }
  * { margin: 0; padding: 0; box-sizing: border-box; }
  html, body {
    width: 1200px;
    height: 900px;
    overflow: hidden;
    background: var(--backdrop);
  }
  .canvas {
    position: relative;
    width: 1200px;
    height: 900px;
    display: flex;
    flex-direction: column;
    align-items: center;
    justify-content: center;
    gap: 44px;
  }
  .card {
    width: 600px;
    height: 343px;
    background: var(--card-black);
    box-shadow: 0 18px 40px rgba(0, 0, 0, 0.55);
    display: flex;
    flex-direction: column;
    align-items: center;
    justify-content: center;
  }
  .gold-text {
    background: linear-gradient(100deg, var(--gold-deep) 0%, var(--gold-mid) 30%, var(--gold-light) 55%, var(--gold-mid) 78%, var(--gold-deep) 100%);
    -webkit-background-clip: text;
    background-clip: text;
    color: transparent;
  }
  .card__name {
    font-family: "Poiret One", "Josefin Sans", sans-serif;
    font-size: 58px;
    font-weight: 400;
    letter-spacing: 2px;
  }
  .card__services {
    font-family: "Josefin Sans", sans-serif;
    font-weight: 300;
    font-size: 20px;
    letter-spacing: 1px;
  }
  .card__phone {
    font-family: "Josefin Sans", sans-serif;
    font-weight: 300;
    font-size: 22px;
    letter-spacing: 2px;
    margin-top: 4px;
  }
</style>
</head>
<body>
  <main class="canvas">
    <section class="card card--front">
      <h1 class="card__name gold-text">Lana Frost</h1>
    </section>
    <section class="card card--back">
      <p class="card__services gold-text">Events · Entertainment · Promotions</p>
      <p class="card__phone gold-text">0491 7265 80</p>
    </section>
  </main>
</body>
</html>
```